Looking for highly visual rework of current Maple Hollow Lodges Wordpress site

Visually Appealing, high tech rework of an existing wordpress site - I want an exquisite sales tool for these gorgeous tiny houses.

Must have the ability to apply various colors and styles to model homes during the sales process. We need to easily create, view, change and save home and color configurations for customers. [Roof Color, Siding, Trim, etc]

Target Market(s)

women, 50 and up

Coding

Coded - Design and coding required

Number of Pages Required

1 page

Font styles to use
Serif

Requirements
Must have
• wordpress compatability
• video of Maple Hollow intro

```html
<!DOCTYPE html>
<html lang="en">
<head>
<meta charset="utf-8">
<title>Maple Hollow Lodges</title>
<link rel="stylesheet" href="https://fonts.googleapis.com/css2?family=Oswald:wght@400;500;600&family=Roboto+Condensed:wght@400;700&family=Nunito+Sans:wght@400;600;700&display=swap">
<style>
:root{
  --wood:#8b4d24;
  --wood-dark:#4b2a17;
  --wood-deep:#3a2012;
  --rust:#a3491d;
  --rust-dark:#7d3412;
  --copper-1:#e79a4f;
  --copper-2:#b55a1f;
  --copper-3:#7f3a12;
  --accent:#d9742a;
  --heading:#7b4a28;
  --beige:#ead7b1;
  --beige-line:#b98a5a;
  --ink:#3e3026;
  --muted:#5f5246;
  --white:#ffffff;
  --bubble:#efefef;
  --chev:#4a4440;
}
*{box-sizing:border-box;margin:0;padding:0}
html,body{width:1200px;height:5028px;overflow:hidden;background:var(--white)}
body{position:relative;font-family:"Nunito Sans",Arial,sans-serif;color:var(--ink)}
.page{position:relative;width:1200px;height:5028px;overflow:hidden}
section,header,footer{position:absolute;left:0;width:1200px}
.abs{position:absolute}

/* Shared */
.section-title{position:absolute;left:0;width:100%;text-align:center;font-family:"Oswald",sans-serif;font-weight:500;font-size:38px;letter-spacing:.5px;color:var(--heading);text-transform:uppercase}
.section-title .hl{color:var(--accent)}
.btn{display:inline-flex;align-items:center;justify-content:center;height:48px;padding:0 26px;font-family:"Oswald",sans-serif;font-size:18px;letter-spacing:.5px;color:var(--white);text-transform:uppercase;background:linear-gradient(180deg,var(--copper-1),var(--copper-2) 55%,var(--copper-3));border:1px solid #5e2a0c;border-radius:3px;box-shadow:0 3px 6px rgba(0,0,0,.3)}
.divider{position:absolute;left:0;width:1200px;height:64px;display:flex;align-items:center;justify-content:center;gap:8px;z-index:5}
.divider .mark{width:54px;height:54px;border-radius:50%;background:var(--wood);border:3px solid var(--copper-1);display:flex;align-items:center;justify-content:center;font-family:"Oswald",sans-serif;font-size:9px;line-height:1.05;color:var(--white);text-align:center;text-transform:uppercase}

/* Hero */
.hero{top:0;height:620px}
.hero-photo{position:absolute;inset:0;background:linear-gradient(180deg,#6f7c8c 0%,#9aa4ad 28%,#a55a2c 45%,#8a4a25 62%,#6a3b20 74%,#6f7f3e 84%,#4f6430 100%)}
.nav{position:absolute;left:94px;top:100px;width:1012px;height:50px;border-radius:25px;background:linear-gradient(180deg,var(--copper-1),var(--copper-2) 60%,var(--copper-3));box-shadow:0 3px 8px rgba(0,0,0,.4);display:flex;align-items:center;padding:0 24px}
.nav a{font-family:"Oswald",sans-serif;font-size:15px;color:#3a1a08;text-decoration:none;text-transform:uppercase;margin-right:30px}
.nav .right{margin-left:auto;display:flex}
.nav .right a{margin-right:0;margin-left:30px}
.brand{position:absolute;left:493px;top:80px;width:214px;height:112px;border-radius:14px;background:var(--wood);border:3px solid var(--copper-1);display:flex;align-items:center;justify-content:center;gap:10px;box-shadow:0 4px 10px rgba(0,0,0,.4)}
.brand .dot{width:22px;height:22px;border-radius:50%;background:var(--copper-1)}
.brand .name{font-family:"Oswald",sans-serif;font-size:22px;color:var(--white);text-transform:uppercase}

/* Welcome */
.welcome{top:620px;height:308px;background:linear-gradient(180deg,#955430,var(--wood) 50%,#7a4220);text-align:center;color:var(--white)}
.welcome h1{position:absolute;top:42px;width:100%;font-family:"Oswald",sans-serif;font-weight:500;font-size:40px}
.welcome p{position:absolute;left:200px;top:106px;width:800px;font-family:"Roboto Condensed",sans-serif;font-weight:700;font-size:18px;line-height:22px}
.welcome .btn{position:absolute;left:507px;top:190px;width:186px}

/* Build */
.build{top:928px;height:1418px;background:var(--beige)}
.build .section-title{top:98px}
.steps{position:absolute;left:110px;top:180px;width:980px;display:flex;justify-content:space-between}
.step{width:300px;text-align:center}
.step svg{width:64px;height:64px}
.step p{margin-top:24px;font-family:"Roboto Condensed",sans-serif;font-weight:700;font-size:18px;line-height:24px;color:var(--muted)}
.accordion{position:absolute;left:94px;top:399px;width:1012px;display:flex;flex-direction:column;gap:15px}
.acc-item{background:var(--white);border:2px solid var(--beige-line);height:62px;display:flex;align-items:center;padding:0 20px;position:relative}
.acc-item .label{font-family:"Oswald",sans-serif;font-weight:500;font-size:19px;color:var(--ink);text-transform:uppercase}
.acc-item .chev{position:absolute;right:16px;top:50%;margin-top:-15px;width:30px;height:30px;border-radius:50%;background:var(--chev)}
.acc-item.open{height:389px;align-items:flex-start;padding-top:16px}
.acc-item.open .label{color:var(--accent)}
.acc-item.open .chev{top:16px;margin-top:0;background:var(--accent)}
.plans{position:absolute;left:20px;top:60px;width:968px;display:flex;justify-content:space-between}
.plan{width:470px}
.plan .choice{display:flex;align-items:center;gap:10px;font-size:17px;color:var(--muted);margin-bottom:20px}
.radio{width:16px;height:16px;border-radius:50%;border:2px solid #8a8a8a;background:var(--white)}
.radio.on{background:radial-gradient(circle,#555 0 4px,var(--white) 5px)}
.plan-img{width:452px;height:240px;background:linear-gradient(180deg,#f4f1ea 0 45%,#e3d8c6 45% 55%,#f4f1ea 55%);border:3px solid #222}
.quote-actions{position:absolute;left:0;top:1308px;width:100%;display:flex;justify-content:center;gap:14px}

/* About */
.about{top:2346px;height:470px;background:var(--white)}
.about .section-title{left:94px;top:126px;width:auto;text-align:left}
.about p{position:absolute;left:94px;top:186px;width:680px;font-size:19px;line-height:28px;color:var(--ink)}
.about .btn{position:absolute;left:94px;top:328px;width:186px}
.about-photo{position:absolute;left:838px;top:96px;width:300px;height:300px;border-radius:50%;border:6px solid var(--wood);background:linear-gradient(160deg,#8a9aa3,#b06a3a 50%,#6e7f46)}

/* Gallery */
.gallery{top:2816px;height:720px;background:linear-gradient(90deg,var(--wood-deep),var(--wood-dark) 30%,#5a331c 60%,var(--wood-deep))}
.gallery .section-title{top:124px;color:var(--white)}
.shot{position:absolute;background:linear-gradient(170deg,#9aa6b0,#a65b2d 55%,#6d7b45)}
.shot.interior{background:linear-gradient(170deg,#c79a6a,#7c4a28 60%,#3e2616)}

/* Testimonials */
.testimonials{top:3536px;height:486px;background:var(--white)}
.testimonials .section-title{top:96px}
.review{position:absolute;top:174px;width:316px;height:210px}
.review .bubble{width:100%;height:150px;background:var(--bubble);border-radius:6px;padding:18px 20px 0 48px;font-size:17px;line-height:22px;color:var(--muted);position:relative}
.review .q{position:absolute;font-family:Georgia,serif;font-weight:700;font-size:40px;line-height:1;color:var(--ink)}
.review .name{position:absolute;left:0;top:178px;font-weight:700;font-size:18px;color:var(--ink)}
.review .avatar{position:absolute;right:0;top:120px;width:110px;height:110px;border-radius:50%;border:4px solid var(--accent);background:linear-gradient(180deg,#d9cfc4,#b8a696)}

/* Contact */
.contact{top:4022px;height:597px;background:var(--beige)}
.contact .section-title{top:106px}
.contact .sub{position:absolute;top:190px;width:100%;text-align:center;font-family:"Roboto Condensed",sans-serif;font-weight:700;font-size:17px;color:var(--ink);text-transform:uppercase}
.field{position:absolute;background:var(--beige);border:2px solid #8a6848;padding:10px 14px;font-size:18px;font-weight:600;color:var(--ink)}
.contact .btn{position:absolute;left:508px;top:468px;width:184px}

/* Footer */
.footer{top:4619px;height:359px;background:var(--rust);color:var(--white)}
.footer-brand{position:absolute;left:67px;top:40px;width:218px;height:168px;border-radius:16px;background:var(--wood);border:3px solid var(--copper-1);display:flex;align-items:center;justify-content:center;gap:10px}
.footer-brand .dot{width:22px;height:22px;border-radius:50%;background:var(--copper-1)}
.footer-brand .name{font-family:"Oswald",sans-serif;font-size:22px;text-transform:uppercase}
.fcol{position:absolute;top:52px}
.fcol h4{font-family:"Oswald",sans-serif;font-weight:500;font-size:20px;padding-bottom:10px;border-bottom:1px solid rgba(255,255,255,.45);margin-bottom:18px}
.fcol ul{list-style:none;font-size:17px;line-height:27px}
.contact-line{display:flex;gap:10px;font-size:17px;line-height:24px;margin-bottom:22px}
.contact-line svg{flex:none;width:22px;height:22px;margin-top:1px}
.fcol p{font-size:17px;line-height:24px}
.email-pill{margin-top:16px;width:200px;height:30px;border-radius:15px;background:var(--white);color:#777;font-size:14px;padding:6px 14px}
.subscribe{margin-top:12px;width:128px;height:30px;border-radius:15px;background:#f1c9a0;color:var(--rust-dark);font-family:"Oswald",sans-serif;font-size:14px;display:flex;align-items:center;justify-content:center;text-transform:uppercase}
.copyright{position:absolute;top:4978px;left:0;width:1200px;height:50px;background:var(--rust-dark);display:flex;align-items:center;padding:0 24px;color:var(--white);font-size:13px;text-transform:uppercase}
.social{margin-left:auto;display:flex;gap:8px}
.social span{width:22px;height:22px;border-radius:50%;background:var(--copper-1)}
</style>
</head>
<body>
<div class="page">

<header class="hero">
  <div class="hero-photo" role="img" aria-label="Photo collage of three tiny cabins with red roofs, wooden siding and porches on a lawn"></div>
  <nav class="nav">
    <a>Home</a><a>Build Your Own</a><a>About</a>
    <div class="right"><a>Gallery</a><a>Testimonials</a><a>Contact</a></div>
  </nav>
  <div class="brand"><span class="dot"></span><span class="name">Maple Hollow</span></div>
</header>

<section class="welcome">
  <h1>Welcome to Maple Hollow Lodges</h1>
  <p>Lorem ipsum dolor sit amet, consectetur adipiscing elit, sed do eiusmod tempor incididunt ut labore et dolore magna aliqua. Ut enim ad minim veniam, quis nostrud exercitation ullamco laboris nisi ut aliquip ex ea.</p>
  <span class="btn">Learn More</span>
</section>

<div class="divider" style="top:898px"><span class="mark">Maple<br>Hollow</span></div>

<section class="build">
  <h2 class="section-title">Build <span class="hl">Your Own</span></h2>
  <div class="steps">
    <div class="step">
      <svg viewBox="0 0 64 64" fill="none" stroke="#d9742a" stroke-width="4"><circle cx="32" cy="36" r="22"/><path d="M26 8h12M32 8v6M32 36V24M32 36l8 6"/></svg>
      <p>Take 5-10 minutes to design your<br>perfect Maple Hollow cabin</p>
    </div>
    <div class="step">
      <svg viewBox="0 0 64 64" fill="none" stroke="#d9742a" stroke-width="4"><rect x="12" y="8" width="40" height="52" rx="3"/><rect x="24" y="4" width="16" height="8"/><path d="M20 26l4 4 6-8M34 26h12M20 42l4 4 6-8M34 42h12"/></svg>
      <p>Choose the items you want,<br>skip the rest.</p>
    </div>
    <div class="step">
      <svg viewBox="0 0 64 64" fill="none" stroke="#d9742a" stroke-width="4"><rect x="10" y="10" width="44" height="44" stroke-dasharray="6 5"/><path d="M32 18v22M24 32l8 8 8-8M22 46h20"/></svg>
      <p>Download your FREE detailed,<br>printable quote when you are done</p>
    </div>
  </div>

  <div class="accordion">
    <div class="acc-item"><span class="label">Cabin Model</span><span class="chev"></span></div>
    <div class="acc-item open"><span class="label">Floor Plan</span><span class="chev"></span>
      <div class="plans">
        <div class="plan">
          <div class="choice"><span class="radio on"></span>Willow Plan</div>
          <div class="plan-img" role="img" aria-label="Floor plan drawing of the Willow Plan with open-to-below loft and ground floor rooms"></div>
        </div>
        <div class="plan">
          <div class="choice"><span class="radio"></span>Aspen Plan</div>
          <div class="plan-img" role="img" aria-label="Floor plan drawing of the Aspen Plan with loft, great room, kitchen and bedroom"></div>
        </div>
      </div>
    </div>
    <div class="acc-item"><span class="label">Exterior</span><span class="chev"></span></div>
    <div class="acc-item"><span class="label">Interior</span><span class="chev"></span></div>
    <div class="acc-item"><span class="label">Kitchen &amp; Bath</span><span class="chev"></span></div>
    <div class="acc-item"><span class="label">Utilities</span><span class="chev"></span></div>
    <div class="acc-item"><span class="label">Delivery &amp; More</span><span class="chev"></span></div>
  </div>

  <div class="quote-actions"><span class="btn">Download Quote</span><span class="btn">Email Me My Quote</span></div>
</section>

<div class="divider" style="top:2314px"><span class="mark">Maple<br>Hollow</span></div>

<section class="about">
  <h2 class="section-title">About <span class="hl">Maple Hollow</span></h2>
  <p>Lorem ipsum dolor sit amet, consectetur adipiscing elit, sed do eiusmod tempor incididunt ut labore et dolore magna aliqua. Ut enim ad minim veniam, quis nostrud exercitation ullamco la boris nisi ut aliquip ex ea commodo consequat.</p>
  <span class="btn">Learn More</span>
  <div class="about-photo" role="img" aria-label="Round photo of a wooden tiny cabin with a front porch and steps"></div>
</section>

<div class="divider" style="top:2784px"><span class="mark">Maple<br>Hollow</span></div>

<section class="gallery">
  <h2 class="section-title" style="color:#fff">Maple Hollow <span class="hl">Gallery</span></h2>
  <div class="shot" style="left:94px;top:201px;width:369px;height:218px" role="img" aria-label="Photo of a long red-roofed cabin on a lot"></div>
  <div class="shot" style="left:489px;top:201px;width:312px;height:194px" role="img" aria-label="Photo of a cabin with porch and steps"></div>
  <div class="shot" style="left:828px;top:201px;width:278px;height:194px" role="img" aria-label="Photo of a cabin with a screened porch"></div>
  <div class="shot interior" style="left:489px;top:419px;width:194px;height:218px" role="img" aria-label="Photo of a wooden cabin interior"></div>
  <div class="shot interior" style="left:711px;top:419px;width:162px;height:218px" role="img" aria-label="Photo of a cabin porch seating area"></div>
  <div class="shot interior" style="left:898px;top:419px;width:208px;height:218px" role="img" aria-label="Photo of a cabin loft and kitchen"></div>
</section>

<div class="divider" style="top:3504px"><span class="mark">Maple<br>Hollow</span></div>

<section class="testimonials">
  <h2 class="section-title">Words <span class="hl">From Our Customers</span></h2>
  <div class="review" style="left:94px">
    <div class="bubble"><span class="q" style="left:14px;top:14px">&ldquo;</span>Lorem ipsum dolor sit amet, consectetur adipiscing elit, sed diam nonummy nibh eu ismod tincidunt ut laoreet dolor.<span class="q" style="position:relative;font-size:30px"> &rdquo;</span></div>
    <div class="name">Carol Whitman</div>
    <div class="avatar" role="img" aria-label="Customer portrait"></div>
  </div>
  <div class="review" style="left:442px">
    <div class="bubble"><span class="q" style="left:14px;top:14px">&ldquo;</span>Lorem ipsum dolor sit amet, consectetur adipiscing elit, sed diam nonummy nibh eu ismod tincidunt ut laoreet dolor.<span class="q" style="position:relative;font-size:30px"> &rdquo;</span></div>
    <div class="name">Celia Dawson</div>
    <div class="avatar" role="img" aria-label="Customer portrait"></div>
  </div>
  <div class="review" style="left:790px">
    <div class="bubble"><span class="q" style="left:14px;top:14px">&ldquo;</span>Lorem ipsum dolor sit amet, consectetur adipiscing elit, sed diam nonummy nibh eu ismod tincidunt ut laoreet dolor.<span class="q" style="position:relative;font-size:30px"> &rdquo;</span></div>
    <div class="name">Jonah Hartley</div>
    <div class="avatar" role="img" aria-label="Customer portrait"></div>
  </div>
</section>

<div class="divider" style="top:3990px"><span class="mark">Maple<br>Hollow</span></div>

<section class="contact">
  <h2 class="section-title">Contact <span class="hl">Us</span></h2>
  <div class="sub">Let us know what you need</div>
  <div class="field" style="left:94px;top:242px;width:336px;height:44px">Your Name</div>
  <div class="field" style="left:446px;top:242px;width:312px;height:44px">Your Email</div>
  <div class="field" style="left:771px;top:242px;width:335px;height:44px">Your Subject</div>
  <div class="field" style="left:94px;top:302px;width:1012px;height:124px">Message</div>
  <span class="btn">Submit</span>
</section>

<footer class="footer">
  <div class="footer-brand"><span class="dot"></span><span class="name">Maple Hollow</span></div>
  <div class="fcol" style="left:335px;width:170px">
    <h4>Quick Links</h4>
    <ul><li>Home</li><li>Build Your Own</li><li>About</li><li>Gallery</li><li>Testimonials</li><li>Contact</li></ul>
  </div>
  <div class="fcol" style="left:550px;width:240px">
    <h4>Contact</h4>
    <div class="contact-line"><svg viewBox="0 0 24 24" fill="none" stroke="#fff" stroke-width="2"><circle cx="12" cy="12" r="10"/><path d="M12 17s-4-4-4-7a4 4 0 018 0c0 3-4 7-4 7z"/></svg><span>123 Lorem Ipsum Dr.<br>Suite #100<br>Fairbrook, CA 90111</span></div>
    <div class="contact-line"><svg viewBox="0 0 24 24" fill="none" stroke="#fff" stroke-width="2"><circle cx="12" cy="12" r="10"/><path d="M9 7l2 3-1.5 1.5a7 7 0 003 3L14 13l3 2-1 2c-4 0-9-5-9-9z"/></svg><span>1800.555.0147</span></div>
    <div class="contact-line"><svg viewBox="0 0 24 24" fill="none" stroke="#fff" stroke-width="2"><circle cx="12" cy="12" r="10"/><rect x="7" y="8.5" width="10" height="7"/><path d="M7 9l5 4 5-4"/></svg><span>info@maplehollow.com</span></div>
  </div>
  <div class="fcol" style="left:858px;width:250px">
    <h4>Newsletter</h4>
    <p>Register your email address to get more information about us</p>
    <div class="email-pill">Email Address</div>
    <div class="subscribe">Subscribe</div>
  </div>
</footer>

<div class="copyright">
  <span>Copyright © 2016 Maple Hollow Lodges. All rights reserved.</span>
  <div class="social"><span></span><span></span><span></span></div>
</div>

</div>
</body>
</html>
```